Stonebay Towing Business Card

Towing
Accident towing
Mechanical breakdown
Insurance, salvage and recovery
4wd off road towing
Light & Heavy towing
8347 2516
24 hour business 7 days

Logo can be whole size on front

Industry/Entity Type

Towing/ transport

Contact Information for Business Card

The above

```html
<!DOCTYPE html>
<html lang="en">
<head>
<meta charset="utf-8">
<title>Stonebay Towing Business Card</title>
<link rel="stylesheet" href="https://fonts.googleapis.com/css2?family=Arimo:wght@400;700&display=swap">
<style>
  :root {
    --bg: #2e2e2e;
    --paper: #f7f7f7;
    --ink: #0b0b0b;
    --red: #c81e24;
    --white: #ffffff;
  }
  * { margin: 0; padding: 0; box-sizing: border-box; }
  html, body { width: 1200px; height: 900px; overflow: hidden; }
  body {
    background: var(--bg);
    font-family: "Arimo", Arial, sans-serif;
    position: relative;
  }
  .card {
    position: absolute;
    left: 280px;
    width: 640px;
    height: 366px;
    background: var(--paper);
    overflow: hidden;
    box-shadow: 0 10px 24px rgba(0,0,0,0.45);
  }
  .card-info { top: 60px; }
  .card-brand { top: 474px; }
  .wave { position: absolute; inset: 0; width: 100%; height: 100%; }
  .brand-name {
    position: absolute;
    color: var(--red);
    font-weight: 700;
    white-space: nowrap;
    letter-spacing: 0.5px;
  }
  .card-info .brand-name { top: 34px; right: 40px; font-size: 32px; }
  .card-brand .brand-name {
    top: 50%; left: 50%;
    transform: translate(-50%, -50%);
    font-size: 60px;
  }
  .services {
    position: absolute;
    right: 30px;
    top: 142px;
    list-style: none;
    text-align: right;
    color: var(--white);
    font-size: 14px;
    font-weight: 700;
    line-height: 19px;
  }
  .services li::after {
    content: "\2713";
    color: var(--red);
    margin-left: 5px;
  }
  .contact {
    position: absolute;
    left: 46px;
    bottom: 36px;
    color: var(--white);
  }
  .phone-line {
    display: flex;
    align-items: center;
    gap: 12px;
    font-size: 34px;
    font-weight: 400;
    letter-spacing: 1px;
  }
  .phone-icon { width: 30px; height: 30px; }
  .hours {
    font-size: 34px;
    font-weight: 700;
    margin-top: 4px;
    letter-spacing: 0.5px;
  }
</style>
</head>
<body>
  <section class="card card-info">
    <svg class="wave" viewBox="0 0 640 366" preserveAspectRatio="none" aria-hidden="true">
      <path fill="var(--red)" d="M0,250 C90,205 170,168 320,140 C450,118 560,108 640,66 L640,366 L0,366 Z"/>
      <path fill="var(--ink)" d="M0,292 C70,282 150,272 205,228 C270,180 430,150 640,104 L640,366 L0,366 Z"/>
      <path fill="none" stroke="var(--white)" stroke-width="2" opacity="0.8" d="M160,232 C190,200 240,180 300,168"/>
    </svg>
    <div class="brand-name">Stonebay Towing</div>
    <ul class="services">
      <li>Towing</li>
      <li>Accident towing</li>
      <li>Mechanical breakdown</li>
      <li>Insurance, salvage and recovery</li>
      <li>4wd off road towing</li>
      <li>Light &amp; Heavy towing</li>
    </ul>
    <div class="contact">
      <div class="phone-line">
        <svg class="phone-icon" viewBox="0 0 24 24" aria-hidden="true">
          <path fill="var(--red)" d="M6.6 10.8c1.4 2.8 3.8 5.1 6.6 6.6l2.2-2.2c.3-.3.7-.4 1-.2 1.1.4 2.3.6 3.6.6.6 0 1 .4 1 1V20c0 .6-.4 1-1 1C10.6 21 3 13.4 3 4c0-.6.4-1 1-1h3.5c.6 0 1 .4 1 1 0 1.3.2 2.5.6 3.6.1.3 0 .7-.2 1z"/>
          <path fill="none" stroke="var(--red)" stroke-width="1.6" stroke-linecap="round" d="M14 3.5a7 7 0 0 1 6.5 6.5M14 7a3.5 3.5 0 0 1 3 3"/>
        </svg>
        <span>8347 2516</span>
      </div>
      <div class="hours">24/7 Business</div>
    </div>
  </section>

  <section class="card card-brand">
    <div class="brand-name">Stonebay Towing</div>
  </section>
</body>
</html>
```